Business Card Design

Hello!
We would like you to design some business cards for us. We will send you a sample of what we have. We want to take out the Tidewell Harbor Logo and add the RZD logo. This is the company that we own and it manages 7 to 8 franchised child care locations called Pebble Grove. So you can make the Pebble Grove a little logo smaller than what it currently is. Currently the back of the card lists the locations but we don't need that as we are adding new locations every few months. We can also add the website address for RZD below the logo if needed. We don't like the current design so please change it up as you like. Please let us know if you have any questions.

Industry/Entity Type

Business

Contact Information for Business Card

See above

Font styles to use
Serif
Sans Serif

Colors

Designer to choose colors to be used in the design.

Requirements
Must have
• Clean crisp look

```html
<!DOCTYPE html>
<html lang="en">
<head>
<meta charset="utf-8">
<title>Pebble Grove – RZD Business Card</title>
<link rel="stylesheet" href="https://fonts.googleapis.com/css2?family=Open+Sans:wght@400;600;700&display=swap">
<style>
  :root{
    --bg:#e9e7e4;
    --charcoal:#2f2f31;
    --charcoal-text:#6d6d70;
    --paper:#ffffff;
    --red:#c8202f;
    --red-dark:#a51c28;
    --ink:#2b2b2b;
    --grey:#5a5a5a;
  }
  *{box-sizing:border-box;margin:0;padding:0}
  html,body{width:1200px;height:800px;overflow:hidden}
  body{background:var(--bg);font-family:"Open Sans",Arial,sans-serif;position:relative}
  .card{position:absolute;width:540px;height:310px;border-radius:18px;overflow:hidden;box-shadow:0 4px 14px rgba(0,0,0,.18)}
  .card--front{left:40px;top:245px;background:var(--charcoal)}
  .card--back{left:620px;top:245px;background:var(--paper)}

  .brand-academy{position:absolute;text-transform:uppercase;letter-spacing:3px;font-weight:600}
  .brand-academy__name{font-size:26px;line-height:1}
  .brand-academy__tag{font-size:11px;letter-spacing:2.5px;margin-top:6px;font-weight:400}
  .card--front .brand-academy{left:48px;top:118px;color:var(--charcoal-text)}
  .card--front .brand-academy__name{color:#8a6e72}
  .card--back .brand-academy{left:190px;top:30px}
  .card--back .brand-academy__name{color:var(--red);font-size:24px}
  .card--back .brand-academy__tag{color:var(--grey)}

  .brand-rzd{position:absolute;text-align:left}
  .brand-rzd__mark{display:flex;align-items:center;gap:8px}
  .brand-rzd__square{width:18px;height:18px;background:var(--red)}
  .brand-rzd__name{font-weight:700;font-size:24px;letter-spacing:3px;color:var(--red)}
  .brand-rzd__full{font-weight:700;font-size:10px;letter-spacing:1px;text-transform:uppercase;margin-top:4px;line-height:1.3}
  .card--front .brand-rzd{left:340px;top:48px}
  .card--front .brand-rzd__full{color:#b9555e}
  .card--back .brand-rzd{left:370px;top:112px}
  .card--back .brand-rzd__full{color:var(--red)}

  .web{position:absolute;font-size:12px;color:var(--red);letter-spacing:.3px}
  .card--front .web{right:34px;top:170px;color:#b9555e}
  .card--back .web{right:30px;top:204px}

  .rule{position:absolute;height:2px;background:var(--red)}
  .card--front .rule{left:0;right:34px;top:196px}
  .card--back .rule--web{left:300px;right:30px;top:228px}
  .card--back .rule--bottom{left:0;right:0;bottom:16px;height:3px}

  .header-band{position:absolute;left:0;top:0;width:540px;height:120px}

  .person{position:absolute;left:20px;top:118px;padding-left:14px;border-left:6px solid var(--red)}
  .person__name{font-size:22px;font-weight:600;color:var(--ink);line-height:1.1}
  .person__title{font-size:12px;color:var(--red)}

  .contacts{position:absolute;left:26px;top:180px;font-size:12px;color:var(--grey);line-height:1.45;list-style:none}
  .contacts li{display:flex;align-items:flex-start;gap:10px;margin-bottom:4px}
  .contacts svg{flex:none;margin-top:2px}
</style>
</head>
<body>

<section class="card card--front" aria-label="Card front">
  <div class="brand-rzd">
    <div class="brand-rzd__mark"><span class="brand-rzd__square"></span><span class="brand-rzd__name">RZD</span></div>
    <div class="brand-rzd__full">Rosewood Daycare<br>Management</div>
  </div>
  <div class="brand-academy">
    <div class="brand-academy__name">Pebble Grove</div>
    <div class="brand-academy__tag">Educational Child Care</div>
  </div>
  <div class="web">pebblegrove.net</div>
  <div class="rule"></div>
</section>

<section class="card card--back" aria-label="Card back">
  <svg class="header-band" viewBox="0 0 540 120" aria-hidden="true">
    <polyline points="0,104 250,104 290,84 540,84" fill="none" stroke="#c8202f" stroke-width="3"/>
    <polyline points="0,110 252,110 292,90 540,90" fill="none" stroke="#a51c28" stroke-width="1"/>
  </svg>
  <div class="brand-academy">
    <div class="brand-academy__name">Pebble Grove</div>
    <div class="brand-academy__tag">Educational Child Care</div>
  </div>
  <div class="brand-rzd">
    <div class="brand-rzd__mark"><span class="brand-rzd__square"></span><span class="brand-rzd__name">RZD</span></div>
    <div class="brand-rzd__full">Rosewood Daycare<br>Management</div>
  </div>

  <div class="person">
    <div class="person__name">Dana Morrow</div>
    <div class="person__title">Academy Owner</div>
  </div>

  <ul class="contacts">
    <li>
      <svg width="12" height="14" viewBox="0 0 12 14"><path d="M6 0a5 5 0 0 1 5 5c0 3.5-5 9-5 9S1 8.5 1 5a5 5 0 0 1 5-5z" fill="#c8202f"/><circle cx="6" cy="5" r="2" fill="#fff"/></svg>
      <span>Management Offices<br>418 Linden Park Road, Suite B<br>Maple Ridge, IL 60412</span>
    </li>
    <li>
      <svg width="13" height="10" viewBox="0 0 13 10"><rect width="13" height="10" rx="1" fill="#c8202f"/><path d="M0.5 1l6 4.5 6-4.5" fill="none" stroke="#fff" stroke-width="1.2"/></svg>
      <span>dana.morrow@pebblegrove.net</span>
    </li>
    <li>
      <svg width="13" height="12" viewBox="0 0 13 12"><path d="M1 4c0-2 2-3 5.5-3S12 2 12 4l-2.5 1-1-1.5h-4l-1 1.5z" fill="#c8202f"/><rect x="2" y="6" width="9" height="6" rx="1" fill="#c8202f"/></svg>
      <span>630.555.0147</span>
    </li>
  </ul>

  <div class="web">pebblegrove.net</div>
  <div class="rule rule--web"></div>
  <div class="rule rule--bottom"></div>
</section>

</body>
</html>
```